Business Card Design Project

looking for a stylish and simple double sided business card.
I am an artist - specialising in fashion illustration, portraits and murals.
the front should be simply my name and tag:

D U R E S K
Living in colour

My preference is for a Black background with DURESK in red or embossed.
Living in colour in White or multi-coloured.

the back will have detail:

Personalised Art
Portraits, Murals, Fashion Illustration

0437 582 190
duresk@duresk.com.au
www.duresk.com.au

Target Market(s)

Adults that are based in western speaking countries who have an appreciation for art and design. Portraits and wall art
Business owners who may need personalised all art for their business space. Murals and personalised canvass.
People in the fashion industry, who may require fashion illustrations.

Industry/Entity Type

Fashion

Requirements
Must have
• BOLD but simple at the same time, timeless modern element to it.
Nice to have
• simple lettering
Should not have
• Not too busy or wordy,

```html
<!DOCTYPE html>
<html lang="en">
<head>
<meta charset="utf-8">
<title>Duresk — Business Card</title>
<link rel="stylesheet" href="https://fonts.googleapis.com/css2?family=Jost:wght@400&display=swap">
<style>
  :root {
    --stage: #cfcfcf;
    --card: #0d0d0e;
    --card-edge: #1b1b1d;
    --red: #e0232e;
    --red-soft: #c81f29;
    --white: #f2f2f2;
    --grey: #a9a9ab;
    --font: "Jost", "Futura", sans-serif;
  }
  * { margin: 0; padding: 0; box-sizing: border-box; }
  html, body {
    width: 1200px;
    height: 900px;
    overflow: hidden;
    background: var(--stage);
    font-family: var(--font);
  }
  .stage {
    width: 1200px;
    height: 900px;
    display: flex;
    flex-direction: column;
    align-items: center;
    justify-content: center;
    gap: 60px;
  }
  .card {
    position: relative;
    width: 580px;
    height: 352px;
    background: var(--card);
    border: 1px solid var(--card-edge);
    box-shadow: 0 10px 30px rgba(0,0,0,0.25);
  }

  /* Front */
  .brand {
    position: absolute;
    left: 0;
    right: 0;
    top: 138px;
    display: flex;
    align-items: center;
    justify-content: center;
    gap: 16px;
  }
  .brand-mark {
    width: 14px;
    height: 14px;
    background: var(--red);
  }
  .brand-name {
    color: var(--white);
    font-weight: 400;
    font-size: 44px;
    letter-spacing: 0.04em;
    line-height: 1;
  }
  .brand-tag {
    position: absolute;
    left: 0;
    right: 0;
    bottom: 40px;
    text-align: center;
    color: var(--grey);
    font-weight: 400;
    font-size: 15px;
    letter-spacing: 0.02em;
  }

  /* Back */
  .services {
    position: absolute;
    left: 58px;
    top: 62px;
    color: var(--white);
    font-weight: 400;
    font-size: 15px;
    text-transform: uppercase;
    white-space: nowrap;
  }
  .services .dot {
    display: inline-block;
    width: 6px;
    height: 6px;
    border-radius: 50%;
    background: var(--white);
    vertical-align: middle;
    margin: 0 6px 3px;
  }
  .rule {
    position: absolute;
    height: 2px;
    background: var(--red-soft);
  }
  .rule-top { left: 118px; top: 112px; width: 372px; }
  .rule-bottom { left: 72px; top: 240px; width: 340px; }
  .contact {
    position: absolute;
    left: 200px;
    top: 134px;
    list-style: none;
    color: var(--red);
    font-weight: 400;
    font-size: 16px;
    line-height: 29px;
    white-space: nowrap;
  }
  .contact li:first-child { padding-left: 38px; }
  .contact li:nth-child(2) { padding-left: 12px; }
  .tagline-back {
    position: absolute;
    left: 64px;
    top: 268px;
    color: var(--white);
    font-weight: 400;
    font-size: 15px;
    text-transform: uppercase;
  }
</style>
</head>
<body>
  <main class="stage">
    <section class="card card-front" aria-label="Card front">
      <div class="brand">
        <span class="brand-mark" aria-hidden="true"></span>
        <h1 class="brand-name">Duresk</h1>
      </div>
      <p class="brand-tag">Living in colour</p>
    </section>

    <section class="card card-back" aria-label="Card back">
      <p class="services">Portraits<span class="dot"></span>Murals<span class="dot"></span>Fashion Illustration</p>
      <span class="rule rule-top"></span>
      <ul class="contact">
        <li>0437 582 190</li>
        <li>duresk@duresk.com.au</li>
        <li>www.duresk.com.au</li>
      </ul>
      <span class="rule rule-bottom"></span>
      <p class="tagline-back">Personalised Art</p>
    </section>
  </main>
</body>
</html>
```